Water Management Company Letterhead

Looking for a eye-catching design of letterhead for a California based parent company of water management products. The letterhead would need to include the three logos of the sub-companies, with "The Brookline Alliance LLC" (parent company) being the primary focus. Please include the sub-company logos in the following order of significance: Velmora, Drifting Reeds North, and then Tolvastone NE. The color schemes should convey water/enviornment - blues and greens. Most importantly it should be something that will stand out. All logos are uploaded. Thank you for your interest!

Target Market(s)

Environmental conservationists, government agencies, etc.

Industry/Entity Type

Environment

Font styles to use
Serif
Sans Serif

Colors
33a6d7
3276b5
abd037
cadf82
85cae6
85acd3

Requirements
Must have
• eye-catching, blue and green tones pulled from logos, water droplet.

```html
<!DOCTYPE html>
<html lang="en">
<head>
<meta charset="UTF-8">
<title>The Brookline Alliance LLC — Letterhead</title>
<link href="https://fonts.googleapis.com/css2?family=Cinzel:wght@500&family=Open+Sans:wght@400;700&family=Roboto+Condensed:wght@400;700&display=swap" rel="stylesheet">
<style>
  :root {
    --backdrop: #e8e9eb;
    --paper: #ffffff;
    --ink: #2b2b2b;
    --ink-soft: #3a3a3a;
    --navy: #1f3f63;
    --blue: #2a8ac6;
    --blue-deep: #3276b5;
    --green: #9bc53d;
    --brown: #6b4a36;
    --rule: #e3e6e8;
  }
  * { box-sizing: border-box; margin: 0; padding: 0; }
  html, body {
    width: 1200px; height: 1000px; overflow: hidden;
    background: var(--backdrop);
  }
  .canvas { position: relative; width: 1200px; height: 1000px; }
  .letterhead {
    position: absolute; left: 260px; top: 20px;
    width: 680px; height: 960px;
    background: var(--paper);
    box-shadow: 0 6px 24px rgba(0,0,0,0.12);
    overflow: hidden;
    font-family: "Open Sans", sans-serif;
    color: var(--ink);
  }
  .header-waves {
    position: absolute; left: 0; top: 0; width: 680px; height: 140px;
  }
  .brand {
    position: absolute; left: 120px; top: 118px;
    display: flex; align-items: center; gap: 10px;
  }
  .brand-dot {
    width: 14px; height: 14px; border-radius: 50%;
    background: var(--blue);
  }
  .brand-name {
    font-family: "Cinzel", serif; font-weight: 500;
    font-size: 26px; letter-spacing: 1px; color: var(--navy);
    white-space: nowrap;
  }
  .content {
    position: absolute; left: 90px; top: 200px; width: 510px;
  }
  .recipient {
    font-size: 12px; line-height: 1.75; font-weight: 700; color: var(--ink);
    margin-bottom: 30px;
  }
  .letter-body {
    font-size: 11.5px; line-height: 1.8; color: var(--ink-soft);
  }
  .letter-body p { margin-bottom: 20px; }
  .closing {
    margin-top: 14px;
    font-size: 12px; color: var(--ink-soft);
  }
  .signature-area {
    width: 150px; height: 46px; margin: 8px 0 6px;
    background: linear-gradient(90deg, #ececec, #f7f7f7);
    border-radius: 4px;
  }
  .footer {
    position: absolute; left: 40px; right: 40px; bottom: 36px;
    display: grid;
    grid-template-columns: auto auto auto 1fr;
    column-gap: 22px; row-gap: 10px;
    align-items: end;
    font-family: "Roboto Condensed", sans-serif;
  }
  .sub-brand {
    display: flex; align-items: center; gap: 6px;
    font-size: 13px; font-weight: 700; white-space: nowrap;
  }
  .sub-brand .mark { width: 10px; height: 10px; border-radius: 50%; }
  .sub-brand--primary { grid-column: 2; color: var(--blue-deep); }
  .sub-brand--primary .mark { background: var(--blue-deep); }
  .sub-brand--secondary { grid-column: 3; color: var(--blue); }
  .sub-brand--secondary .mark { background: var(--green); }
  .sub-brand--tertiary { grid-column: 4; color: var(--brown); }
  .sub-brand--tertiary .mark { background: var(--brown); border-radius: 0; }
  .contact {
    grid-row: 2;
    font-size: 11px; color: var(--ink); white-space: nowrap;
  }
  .contact .label { color: var(--blue); font-weight: 700; margin-right: 3px; }
  .contact .divider { color: var(--blue); margin-right: 6px; }
</style>
</head>
<body>
<div class="canvas">
  <article class="letterhead">
    <svg class="header-waves" viewBox="0 0 680 140" aria-hidden="true">
      <path d="M0 0 L0 30 C 120 60, 260 100, 390 86 C 500 72, 600 40, 680 22 L680 0 Z" fill="var(--blue)"/>
      <path d="M0 30 C 120 60, 260 100, 390 86 C 270 112, 120 84, 0 54 Z" fill="var(--green)"/>
      <path d="M0 0 L0 14 C 140 40, 280 62, 390 56 C 500 50, 600 18, 680 0 Z" fill="#ffffff" opacity="0"/>
    </svg>

    <div class="brand">
      <span class="brand-dot"></span>
      <span class="brand-name">The Brookline Alliance LLC</span>
    </div>

    <div class="content">
      <div class="recipient">
        <div>To</div>
        <div>Lorem Ipsum is simply</div>
        <div>Lorem Ipsum is Lorem Ipsum is</div>
        <div>Lorem Ipsum is</div>
      </div>

      <section class="letter-body">
        <p>dummy text of the printing and typesetting industry. Lorem Ipsum has been the industry's standard dummy text ever since the 1500s, when an unknown printer took a galley of type and scrambled it to make a type specimen book. It has survived not only five centuries, but also the leap into electronic typesetting, remaining essentially unchanged.</p>
        <p>It is a long established fact that a reader will be distracted by the readable content of a page when looking at its layout. The point of using Lorem Ipsum is that it has a more-or-less normal distribution of letters, as opposed to using 'Content here, content here', making it look like readable English. Many desktop publishing packages and web page editors now use Lorem Ipsum as their default model text, and a search for 'lorem'.</p>
        <p>Contrary to popular belief, Lorem Ipsum is not simply random text. It has roots in a piece of classical Latin literature from 45 BC, making it over 2000 years old. A Latin professor at Marlowe Ridge College in Vermont looked up one of the more obscure Latin words, consectetur, from a Lorem Ipsum passage.</p>
      </section>

      <div class="closing">
        <div>Lorem Ipsum</div>
        <div class="signature-area" role="img" aria-label="Handwritten signature"></div>
        <div>Lorem Ipsum is a dummy</div>
      </div>
    </div>

    <footer class="footer">
      <span class="sub-brand sub-brand--primary"><span class="mark"></span>Velmora</span>
      <span class="sub-brand sub-brand--secondary"><span class="mark"></span>Drifting Reeds North</span>
      <span class="sub-brand sub-brand--tertiary"><span class="mark"></span>Tolvastone NE</span>
      <span class="contact"><span class="label">P:</span>(000) 410-2260</span>
      <span class="contact"><span class="label">E:</span>hello@brookline.example</span>
      <span class="contact"><span class="label">W:</span>www.brookline.example</span>
      <span class="contact"><span class="divider">|</span>0000 E. Harbor Line, Lindmere, CA 0000</span>
    </footer>
  </article>
</div>
</body>
</html>
```